Redesign Web Page

I am looking for a great re-design and possibly a banner for TrueSpark.us. The site is for an online dating (self-development, online dating) book. The purpose is to drive book sales.

Target Market(s)

Women 18-55

```html
<!DOCTYPE html>
<html lang="en">
<head>
<meta charset="utf-8">
<title>True Spark — Become an exceptional you</title>
<link href="https://fonts.googleapis.com/css2?family=Open+Sans:wght@400;600;700&display=swap" rel="stylesheet">
<style>
  :root {
    --coral: #e8685d;
    --coral-deep: #d8574d;
    --coral-haze: #ec7b70;
    --dress-red: #c8232a;
    --dress-dark: #8f1519;
    --white: #ffffff;
    --footer: #3a3f44;
  }
  * { box-sizing: border-box; margin: 0; padding: 0; }
  html, body { width: 1200px; height: 763px; overflow: hidden; }
  body {
    position: relative;
    font-family: "Open Sans", Arial, sans-serif;
    color: var(--white);
    background: var(--coral);
  }
  .hero {
    position: absolute; inset: 0 0 60px 0;
    background: var(--coral);
  }
  .skyline {
    position: absolute; left: 0; top: 0; width: 1200px; height: 670px;
    background:
      linear-gradient(180deg, var(--coral-haze) 0%, var(--coral) 40%, var(--coral-deep) 100%);
    opacity: 0.85;
  }
  .heroine {
    position: absolute; left: 468px; top: 62px; width: 278px; height: 641px;
    border-radius: 120px 120px 40px 40px;
    background:
      radial-gradient(ellipse at 50% 20%, #5a2e2a 0%, transparent 28%),
      linear-gradient(180deg, var(--dress-red) 0%, var(--dress-red) 70%, var(--dress-dark) 100%);
    opacity: 0.9;
  }
  .arrows { position: absolute; left: 0; top: 0; }
  .feature { position: absolute; width: 400px; }
  .feature--right { text-align: right; }
  .feature__title { font-size: 21px; font-weight: 400; line-height: 29px; }
  .feature__kicker { font-size: 21px; font-weight: 400; line-height: 29px; margin-bottom: 27px; }
  .feature__text { font-size: 12.5px; line-height: 20px; margin-top: 14px; }
  .button {
    display: inline-block; margin-top: 9px;
    border: 1px solid var(--white);
    height: 40px; line-height: 38px; padding: 0 22px;
    font-size: 14px; font-weight: 600; color: var(--white); text-decoration: none;
  }
  .site-footer {
    position: absolute; left: 0; bottom: 0; width: 1200px; height: 60px;
    background: var(--footer);
    display: flex; align-items: center;
  }
  .brand {
    margin-left: 68px; font-size: 29px; font-weight: 700; color: var(--white);
  }
  .main-nav { margin-left: 110px; display: flex; gap: 27px; }
  .main-nav a { color: var(--white); text-decoration: none; font-size: 11.5px; }
</style>
</head>
<body>
  <section class="hero">
    <div class="skyline" role="img" aria-label="Faint city skyline photograph tinted coral"></div>
    <div class="heroine" role="img" aria-label="Illustration of a woman in a long red gown wearing a tiara and a pink True Spark sash"></div>

    <svg class="arrows" width="1200" height="703" fill="none" stroke="#fff" stroke-width="1.3" stroke-dasharray="5 4">
      <path d="M287 170 C 330 180, 370 188, 360 200 C 345 222, 300 222, 308 205 C 318 188, 400 200, 455 215"/>
      <path d="M455 215 l-9 -6 M455 215 l-10 3" stroke-dasharray="none"/>
      <path d="M882 170 C 840 180, 800 185, 805 200 C 815 225, 865 222, 858 205 C 850 188, 770 200, 712 215"/>
      <path d="M712 215 l9 -6 M712 215 l10 3" stroke-dasharray="none"/>
      <path d="M218 372 C 260 360, 300 350, 295 335 C 288 318, 235 318, 240 332 C 246 348, 330 338, 390 325"/>
      <path d="M390 325 l-10 -3 M390 325 l-8 6" stroke-dasharray="none"/>
      <path d="M935 400 C 890 385, 860 378, 858 362 C 856 345, 910 342, 910 356 C 910 375, 820 368, 762 353"/>
      <path d="M762 353 l10 -2 M762 353 l8 6" stroke-dasharray="none"/>
    </svg>

    <div class="feature" style="left:80px; top:63px;">
      <h2 class="feature__title">Become an exceptional you</h2>
      <p class="feature__text">Ne dico veniam apeirian mel, mea ne assum errem euripidis, duo an dico gubergren. Accumsan deseruisse te duo.</p>
      <a class="button" href="#">But the Book</a>
    </div>

    <div class="feature feature--right" style="left:724px; top:63px;">
      <h2 class="feature__title">Master yourself from the inside out</h2>
      <p class="feature__text">Sea ex appareat rationibus definiebas. Quot unum euismod vim ei. Equidem incorrupte delicatissimi et mei, usu nostro dicunt percipit et.</p>
      <a class="button" href="#">Read out our Blog</a>
    </div>

    <div class="feature" style="left:80px; top:374px; width:310px;">
      <h2 class="feature__title">Attract quality of people into your life</h2>
      <p class="feature__text">Et est dico habeo interpretaris. Sensibus consetetur cu pri, ei wisi detracto recusabo pro.</p>
      <a class="button" href="#">More Products &amp; Services</a>
    </div>

    <div class="feature feature--right" style="left:724px; top:346px;">
      <p class="feature__kicker">Wink</p>
      <h2 class="feature__title">Wink: You are exceptional!</h2>
      <p class="feature__text">Pro debet tation legendos id, pro audiam torquatos<br>te. Ne dico veniam apeirian mel.</p>
      <a class="button" href="#">Get in touch with us</a>
    </div>
  </section>

  <footer class="site-footer">
    <div class="brand">True Spark</div>
    <nav class="main-nav">
      <a href="#">Home</a>
      <a href="#">The Author</a>
      <a href="#">Blog</a>
      <a href="#">Fan Fair &amp; Fun</a>
      <a href="#">Celeb Endorsements</a>
      <a href="#">Love Stories</a>
      <a href="#">Products &amp; Services</a>
      <a href="#">Contact us</a>
    </nav>
  </footer>
</body>
</html>
```